Spirit Distillery needs website design for velmorastills.com

We are a spirit distillery located in Canberra, Australia. We are just about to begin production on our products: Gin, Coffee vodka, lemon myrtle vodka, and apple and cinnamon vodka.
Velmora is Ancient Greek Mythology meaning "elixir of the Gods" so Greek mythology incorporated in the website, as well as simple and user friendly layout and functionality would be great.
Pages would include:
Welcome page with links to:
Our Products (Gin, Coffee vodka, lemon myrtle vodka, and apple and cinnamon vodka)
Events (what events the distillery is attending or holding at the distillery site)
Shop (for bottle sales)
Stockists (where the bottles are sold)
Cocktail recipe page

```html
<!DOCTYPE html>
<html lang="en">
<head>
<meta charset="utf-8">
<title>Velmora Distillery</title>
<link rel="stylesheet" href="https://fonts.googleapis.com/css2?family=Noto+Serif:wght@400;700&family=Oswald:wght@500&family=Work+Sans:wght@400&display=swap">
<style>
:root{
  --gold:#c9a15a;
  --gold-text:#cfa85a;
  --gold-light:#f1d896;
  --gold-dark:#b98d3f;
  --ink:#1a1a1a;
  --body:#3d3d3d;
  --mist:#f4f4f4;
  --white:#ffffff;
  --black:#000000;
}
*{margin:0;padding:0;box-sizing:border-box}
html,body{width:1200px;height:3390px;overflow:hidden}
body{position:relative;background:var(--white);font-family:"Work Sans",Arial,sans-serif;color:var(--body)}
.abs{position:absolute}
.key-band{position:absolute;left:0;width:1200px;background:var(--gold-light);border-top:2px solid var(--gold-dark);border-bottom:2px solid var(--gold-dark)}
.key-band::after{content:"";position:absolute;left:0;right:0;top:50%;height:2px;margin-top:-1px;background:var(--gold-dark)}
.serif{font-family:"Noto Serif",Georgia,serif}
.nav{font-family:"Oswald","Arial Narrow",sans-serif;font-weight:500;text-transform:uppercase}
.header-nav{left:323px;display:flex;gap:30px;font-size:12px;color:var(--ink)}
.brand{font-family:"Noto Serif",Georgia,serif;font-weight:400;color:var(--gold-text);letter-spacing:3px}
.social{display:flex;gap:6px}
.social span{display:block;width:31px;height:31px;border:1.5px solid var(--gold);border-radius:50%}
.btn{position:absolute;display:flex;align-items:center;justify-content:center;border-radius:30px;background:linear-gradient(180deg,var(--gold-light),var(--gold-dark));font-family:"Noto Serif",Georgia,serif;font-weight:700;font-size:16px;color:#2a2212;box-shadow:0 6px 8px rgba(0,0,0,.25)}
.btn.in-flow{position:relative;flex:none}
.section-title{position:absolute;left:0;width:1200px;display:flex;justify-content:center;align-items:center;gap:18px;font-family:"Noto Serif",Georgia,serif;font-weight:700;font-size:35px;color:var(--gold-text)}
.section-title i{display:block;width:72px;height:13px;border:2px solid var(--gold);background:var(--gold-light)}
.welcome-stack{position:absolute;left:170px;width:860px;top:131px;display:flex;flex-direction:column;align-items:center}
.section-text{font-size:13px;line-height:28px;text-align:center;color:var(--body)}
.cocktail-stack{position:absolute;left:661px;top:60px;width:450px;display:flex;flex-direction:column;align-items:flex-start}
.product-card{position:absolute;top:1318px;width:250px;height:290px;border-radius:12px;background:var(--white);box-shadow:0 2px 10px rgba(0,0,0,.15);display:flex;justify-content:center;align-items:center}
.bottle{width:86px;height:245px;border-radius:30px 30px 14px 14px}
.product-name{position:absolute;top:1627px;width:250px;text-align:center;font-family:"Noto Serif",Georgia,serif;font-weight:700;font-size:15px;color:var(--gold-text)}
.event-title{font-family:"Noto Serif",Georgia,serif;font-weight:700;font-size:16px;line-height:28px;color:var(--ink);text-transform:uppercase}
.event-text{font-size:13px;line-height:28px;color:var(--body)}
.event-item{position:absolute;left:794px;width:300px}
.event-thumb{position:absolute;left:580px;width:196px;height:150px}
.footer-nav{left:0;width:1200px;top:3183px;display:flex;justify-content:center;gap:30px;font-size:13px;color:var(--white)}
.footer-social{left:0;width:1200px;top:3223px;display:flex;justify-content:center;gap:14px}
.footer-social span{display:block;width:60px;height:60px;border-radius:50%;background:var(--gold);border:3px solid var(--gold-light)}
</style>
</head>
<body>

<div class="key-band" style="top:0;height:18px"></div>
<header class="abs" style="top:18px;left:0;width:1200px;height:74px;background:var(--white)">
  <div class="abs brand" style="left:74px;top:10px;font-size:38px">VELMORA</div>
  <nav class="abs nav header-nav" style="top:26px">
    <span>Home</span><span>Our Products</span><span>Events</span><span>Shop</span><span>Stockists</span><span>Cocktail Recipe</span>
  </nav>
  <div class="abs social" style="left:823px;top:20px"><span></span><span></span><span></span><span></span></div>
  <div class="abs" style="left:1000px;top:12px;font-size:13px;color:var(--gold)">Call Us Today!</div>
  <div class="abs serif" style="left:999px;top:32px;font-size:22px;color:var(--ink)">02 6150 4821</div>
</header>
<div class="key-band" style="top:92px;height:20px"></div>

<section class="abs" style="top:112px;left:0;width:1200px;height:579px">
  <div class="abs" role="img" aria-label="Illustration of Greek gods in a classical vase-painting style, one leaping with a flaming torch" style="inset:0;background:radial-gradient(circle at 52% 50%,#b3a592 0,#a89a86 32%,#b46a22 60%,#6a2d14 100%)"></div>
  <h1 class="abs serif" style="left:0;width:1200px;top:180px;text-align:center;font-size:56px;font-weight:700;color:var(--white)">VELMORA DISTILLERY</h1>
  <p class="abs" style="left:170px;width:860px;top:262px;text-align:center;font-size:13px;line-height:28px;color:var(--white)">Lorem ipsum dolor sit amet, consectetur adipiscing elit, sed do eiusmod tempor incididunt ut labore et dolore magna aliqua. Quis ipsum suspendisse ultrices gravida. Risus commodo viverra maecenas accumsan lacus vel facilisis.</p>
  <div class="btn" style="left:514px;top:340px;width:172px;height:52px">GET STARTED</div>
  <div class="abs" style="left:568px;top:544px;display:flex;gap:5px">
    <span style="width:9px;height:9px;border-radius:50%;background:var(--gold-light)"></span>
    <span style="width:9px;height:9px;border-radius:50%;background:var(--white)"></span>
    <span style="width:9px;height:9px;border-radius:50%;background:var(--white)"></span>
    <span style="width:9px;height:9px;border-radius:50%;background:var(--white)"></span>
    <span style="width:9px;height:9px;border-radius:50%;background:var(--white)"></span>
  </div>
</section>
<div class="key-band" style="top:691px;height:23px"></div>

<section class="abs" style="top:714px;left:0;width:1200px;height:453px;background:var(--mist)">
  <h2 class="section-title" style="top:72px"><i></i>WELCOME TO VELMORA<i></i></h2>
  <div class="welcome-stack">
    <p class="section-text">Sed ut perspiciatis unde omnis iste natus error sit voluptatem accusantium doloremque laudantium, totam rem aperiam, eaque ipsa quae ab illo inventore veritatis et quasi architecto beatae vitae dicta sunt explicabo. Nemo enim ipsam voluptatem quia voluptas sit aspernatur aut odit aut fugit, sed quia consequuntur magni dolores eos qui ratione voluptatem sequi nesciunt. Neque porro quisquam est, qui dolorem ipsum quia dolor sit amet, consectetur, adipisci velit, sed quia non numquam eius modi tempora incidunt ut labore et dolore magnam aliquam quaerat voluptatem. Ut enim ad minima veniam, quis nostrum exercitationem ullam corporis suscipit laboriosam, nisi ut aliquid ex ea commodi consequatur?</p>
    <div class="btn in-flow" style="margin-top:20px;width:172px;height:53px">LEARN MORE</div>
  </div>
</section>

<section>
  <h2 class="section-title" style="top:1235px"><i></i>OUR PRODUCTS<i></i></h2>
  <div class="product-card" style="left:147px"><div class="bottle" role="img" aria-label="Bottle of coffee vodka" style="background:linear-gradient(180deg,#7a4a26,#a7794c 55%,#6d3f1f)"></div></div>
  <div class="product-card" style="left:457px"><div class="bottle" role="img" aria-label="Bottle of lemon myrtle vodka" style="background:linear-gradient(180deg,#e4d79a,#c9b270 55%,#e9e0b4)"></div></div>
  <div class="product-card" style="left:766px"><div class="bottle" role="img" aria-label="Bottle of gin" style="background:linear-gradient(180deg,#e6e8e8,#b9a17a 55%,#dfe2e2)"></div></div>
  <div class="product-name" style="left:147px">COFFEE VODKA</div>
  <div class="product-name" style="left:457px">LEMON MYRTLE VODKA</div>
  <div class="product-name" style="left:766px">GIN</div>
</section>

<section class="abs" style="top:1724px;left:0;width:1200px;height:579px">
  <div class="abs" role="img" aria-label="Stone statue arm gripping a lightning bolt against stormy clouds" style="left:0;top:0;width:599px;height:579px;background:radial-gradient(circle at 70% 40%,#9fb3c4 0,#4f6478 40%,#1c2838 100%)"></div>
  <div class="abs" style="left:599px;top:0;width:601px;height:579px;background:var(--gold)"></div>
  <div class="cocktail-stack">
    <h2 class="serif" style="display:flex;align-items:center;gap:12px;font-size:33px;font-weight:700;color:var(--white);line-height:44px"><i style="display:block;width:70px;height:13px;border:2px solid var(--gold-light)"></i>COCKTAIL RECIPE<i style="display:block;width:70px;height:13px;border:2px solid var(--gold-light)"></i></h2>
    <p style="margin-top:14px;width:450px;font-size:13px;line-height:28px;color:var(--white)">Sed ut perspiciatis unde omnis iste natus error sit voluptatem accusantium doloremque laudantium, totam rem aperiam, eaque ipsa quae ab illo inventore veritatis et quasi architecto beatae vitae dicta sunt explicabo. Nemo enim ipsam voluptatem quia voluptas sit aspernatur aut odit aut fugit, sed quia consequuntur magni dolores eos qui ratione voluptatem sequi nesciunt. Neque porro quisquam est, qui dolorem ipsum quia dolor sit amet, consectetur, adipisci velit, sed quia non numquam eius modi tempora incidunt ut labore et dolore magnam aliquam quaerat voluptatem. Ut enim ad minima veniam, quis nostrum exercitationem ullam corporis suscipit laboriosam, nisi ut aliquid ex ea commodi consequatur?</p>
    <div class="btn in-flow" style="margin-top:20px;width:170px;height:50px">LEARN MORE</div>
  </div>
</section>

<section>
  <h2 class="section-title" style="top:2371px"><i></i>OUR EVENTS<i></i></h2>
  <div class="abs" role="img" aria-label="Glasses of lemon cocktail with ice on a wooden table" style="left:124px;top:2463px;width:439px;height:270px;background:linear-gradient(135deg,#3c2414,#c9a04c 45%,#e6dfb8 70%,#5a3a22)"></div>
  <div class="abs" style="left:130px;top:2744px;width:440px">
    <div class="event-title">Lorem ipsum dolor sit amet consecte tur adipiscing elit sed do</div>
    <p class="event-text" style="margin-top:2px">Lorem ipsum dolor sit amet, consectetur adipiscing elit, sed do eius-mod tempor incididunt ut labore et dolore magna aliqua. Quis ipsum suspendisse ultrices gravida Risus commodo.</p>
    <div class="btn in-flow" style="margin-top:16px;width:179px;height:50px">LEARN MORE</div>
  </div>

  <div class="event-thumb" role="img" aria-label="Cocktail glass splashing against a blue background" style="top:2463px;background:radial-gradient(circle at 50% 45%,#cfe6f5,#2a6aa8 55%,#0a2748)"></div>
  <div class="event-thumb" role="img" aria-label="Amber cocktail on a bar counter" style="top:2629px;background:radial-gradient(circle at 65% 50%,#e5a640,#6b3a16 50%,#1a0f08)"></div>
  <div class="event-thumb" role="img" aria-label="Coffee cocktail with ice among coffee beans" style="top:2795px;background:radial-gradient(circle at 55% 45%,#6a5a50,#2c221c 60%,#111)"></div>

  <div class="event-item" style="top:2465px">
    <div class="event-title">Lorem ipsum dolor sit amet iscing elitsed do eiusm</div>
    <p class="event-text" style="margin-top:2px">Lorem ipsum dolor sit amet, consectetur adipiscing elit, sed do eiusmod tempor incid-idunt ut labore et dolore.</p>
  </div>
  <div class="event-item" style="top:2631px">
    <div class="event-title">Lorem ipsum dolor sit amet iscing elitsed do eiusm</div>
    <p class="event-text" style="margin-top:2px">Lorem ipsum dolor sit amet, consectetur adipiscing elit, sed do eiusmod tempor incid-idunt ut labore et dolore.</p>
  </div>
  <div class="event-item" style="top:2797px">
    <div class="event-title">Lorem ipsum dolor sit amet iscing elitsed do eiusm</div>
    <p class="event-text" style="margin-top:2px">Lorem ipsum dolor sit amet, consectetur adipiscing elit, sed do eiusmod tempor incid-idunt ut labore et dolore.</p>
  </div>
</section>

<div class="key-band" style="top:3021px;height:22px"></div>
<footer class="abs" style="top:3043px;left:0;width:1200px;height:326px;background:var(--black)">
  <div class="abs brand" style="left:0;width:1200px;top:80px;text-align:center;font-size:44px">VELMORA</div>
</footer>
<nav class="abs nav footer-nav">
  <span>Home</span><span>Our Products</span><span>Events</span><span>Shop</span><span>Stockists</span><span>Cocktail Recipe</span>
</nav>
<div class="abs footer-social"><span></span><span></span><span></span></div>
<div class="abs" style="left:0;width:1200px;top:3295px;text-align:center;font-size:11.5px;color:var(--white)">© Copyright 2021&nbsp; Velmora &nbsp;&nbsp;&nbsp;|&nbsp;&nbsp;&nbsp; All Rights Reserved</div>
<div class="key-band" style="top:3369px;height:21px"></div>

</body>
</html>
```